Hot young IT advisor needs business cards as upscale and innovative as they are

We need business cards that make a statement about who we are, as a young and upscale IT advisor. Our whole angle is innovation and tenacity in our personal relationships with our clients. We've just done a brand overhaul and need cards that have the new logos, but we're also looking for someone with a sixth sense who can capture what sets us apart and communicate that with a business card. Clean, minimalist, upscale, innovative, personal. Our budget only allows room for them to be soft-touch, no spot gloss or foil designs please.

Target Market(s)

High-level decision makers at middle-market and large organizations in the healthcare, financial services, sports and entertainment, K-12 education, college and university, state and local government, and federal government sectors.

Industry/Entity Type

Information Technology

Font styles to use
Sans Serif

Colors
ec1f27
606060
ffffff

Requirements
Should not have
• Designs with low contrast which would require spot-gloss or embossing.

```html
<!DOCTYPE html>
<html lang="en">
<head>
<meta charset="utf-8">
<title>Norvale business cards</title>
<link rel="stylesheet" href="https://fonts.googleapis.com/css2?family=Roboto:wght@400;500&display=swap">
<style>
  :root {
    --red: #ec1f27;
    --ink: #4a4a4a;
    --grey: #606060;
    --white: #ffffff;
    --backdrop: #e6e6e6;
    --dark-top: #474a45;
    --dark-bottom: #363934;
  }
  * { margin: 0; padding: 0; box-sizing: border-box; }
  html, body { width: 1200px; height: 1200px; overflow: hidden; }
  body {
    background: var(--backdrop);
    font-family: "Roboto", Arial, sans-serif;
    position: relative;
  }
  .card {
    position: absolute;
    left: 257px;
    width: 686px;
    height: 392px;
  }
  .card-front { top: 165px; background: var(--white); }
  .card-back {
    top: 653px;
    background: linear-gradient(to bottom, var(--dark-top), var(--dark-bottom));
  }

  /* front */
  .brand {
    position: absolute;
    left: 30px;
    width: 330px;
    top: 0;
    height: 392px;
    display: flex;
    flex-direction: column;
    align-items: center;
    justify-content: center;
    gap: 18px;
  }
  .brand-mark {
    width: 22px; height: 22px; background: var(--red);
  }
  .brand-name {
    color: var(--red);
    font-weight: 500;
    font-size: 34px;
    letter-spacing: 6px;
  }
  .divider {
    position: absolute;
    left: 373px;
    top: 66px;
    height: 261px;
    width: 2px;
    background: linear-gradient(to bottom, rgba(96,96,96,0), #9a9a9a 30%, #9a9a9a 70%, rgba(96,96,96,0));
  }
  .details {
    position: absolute;
    left: 403px;
    top: 84px;
    color: var(--grey);
  }
  .person-name {
    font-size: 26px;
    font-weight: 500;
    color: var(--ink);
    line-height: 1.1;
  }
  .person-role {
    font-size: 18px;
    font-weight: 500;
    color: var(--red);
    line-height: 1.2;
  }
  .address {
    margin-top: 12px;
    font-size: 16.5px;
    line-height: 21px;
    font-style: normal;
  }
  .contacts { list-style: none; margin-top: 9px; }
  .contacts li {
    display: flex;
    align-items: center;
    gap: 10px;
    font-size: 16.5px;
    line-height: 22px;
  }
  .contacts svg { width: 17px; height: 15px; fill: var(--ink); flex: none; }

  /* back */
  .back-brand {
    position: absolute;
    left: 0; right: 0;
    top: 150px;
    display: flex;
    align-items: center;
    justify-content: center;
    gap: 14px;
  }
  .back-brand .brand-mark { width: 26px; height: 26px; }
  .back-brand .brand-name { font-size: 40px; }
  .back-web {
    position: absolute;
    left: 0; right: 0;
    top: 348px;
    text-align: center;
    color: var(--white);
    font-size: 17px;
    letter-spacing: 5.5px;
  }
</style>
</head>
<body>
  <section class="card card-front">
    <div class="brand">
      <span class="brand-name">NORVALE</span>
    </div>
    <div class="divider"></div>
    <div class="details">
      <h1 class="person-name">Daniel Reyes</h1>
      <p class="person-role">President</p>
      <address class="address">412 Birchwood Court<br>Juneau, Alaska 99801</address>
      <ul class="contacts">
        <li><svg viewBox="0 0 16 16"><path d="M3.5 1l2.5 3-1.5 1.8c.9 2 2.4 3.6 4.5 4.6L10.8 9l3.2 2.4-1.4 2.8C7 14 2 9 1.8 3z"/></svg>555-014-2276</li>
        <li><svg viewBox="0 0 16 16"><path d="M4.5 1h7v14h-7zM6 2.5v10h4v-10z"/></svg>555-017-8830</li>
        <li><svg viewBox="0 0 16 16"><path d="M4 1h7v4H4zM1 6h14v7h-2v-2H3v2H1zM4 12h8v3H4z"/></svg>555-019-4412</li>
        <li><svg viewBox="0 0 16 16"><path d="M1 3h14v10H1zM2.5 4.5L8 8.5l5.5-4z" fill-rule="evenodd"/></svg>hello@norvale.com</li>
        <li><svg viewBox="0 0 16 16"><circle cx="8" cy="8" r="7"/><path d="M5 4c2 0 3 1 2 3s-2 1-3 3M10 9c1 0 2 1 1 3" stroke="#fff" stroke-width="1.6" fill="none"/></svg>www.norvale.com</li>
      </ul>
    </div>
  </section>

  <section class="card card-back">
    <div class="back-brand">
      <span class="brand-name">NORVALE</span>
    </div>
    <p class="back-web">www.norvale.com</p>
  </section>
</body>
</html>
```